International Chino Pant Manufacturer

We need modern packaging design for men's chino. All kinds of packaging designs are welcome.

The pant is folded and packaged in a poly bag. We require a label design for the brand name Tarvo. The main label will be attached by a string on the belt loop. the size of that label will 15cm in length and 5cm wide. This is the first label the customer see's when he picks up the garment. Therefore, we require an eye catching design for that. If required it could have certain information about the chino pant on the main label such as Comfort fit, Wrinkle-resistant, machine washable, luxury fabric. But, if you feel that adding the above information spoils the design of the label then it is not a must to include the above information. On the back of the label we like to include the information that this pant was manufactured in an Ecora Summit certified green plant and hence the damage to the environment because of the plant is nill.

The second label label is attached on to the waist band and the purpose of that label is to include the size of the pant such 32x32. The size of that label is 8cm in length and 4cm in width. There is no design on the back on this label it has to be blank.

Manufacturer

```html
<!DOCTYPE html>
<html lang="en">
<head>
<meta charset="utf-8">
<title>Tarvo Chino Labels</title>
<link rel="stylesheet" href="https://fonts.googleapis.com/css2?family=Arimo:wght@400;700&display=swap">
<style>
  :root {
    --bg: #e4e5e6;
    --tag-brown: #6b2c00;
    --tag-red: #800000;
    --glow-red: #c8280a;
    --tag-khaki: #cccc7e;
    --brand-ink: #1c120a;
    --size-grey: #a8a8a8;
    --label-ink: #111111;
    --eyelet: #111111;
    --eyelet-ring: #9a9a9a;
  }
  * { margin: 0; padding: 0; box-sizing: border-box; }
  html, body {
    width: 1200px;
    height: 1000px;
    overflow: hidden;
    background: var(--bg);
  }
  .canvas {
    position: relative;
    width: 1200px;
    height: 1000px;
    font-family: "Arimo", Arial, sans-serif;
  }
  .tag { position: absolute; }
  .eyelet {
    position: absolute;
    left: 50%;
    top: 40px;
    width: 34px;
    height: 34px;
    margin-left: -17px;
    border-radius: 50%;
    background: var(--eyelet-ring);
    border: 7px solid var(--eyelet);
  }
  .size-tag {
    left: 590px;
    top: 110px;
    width: 390px;
    height: 780px;
    background: var(--tag-khaki);
  }
  .main-tag {
    left: 250px;
    top: 140px;
    width: 400px;
    height: 720px;
    overflow: hidden;
    background: linear-gradient(to bottom, var(--tag-brown) 0, var(--tag-brown) 250px, var(--tag-red) 500px, var(--tag-red) 100%);
  }
  .wave-artwork {
    position: absolute;
    left: 0;
    top: 250px;
    width: 100%;
    height: 250px;
    background: linear-gradient(to bottom, var(--tag-brown), var(--glow-red) 45%, var(--tag-red));
    opacity: 0.9;
  }
  .brand-name {
    position: absolute;
    top: 150px;
    left: 0;
    right: 0;
    text-align: center;
    font-weight: 700;
    font-size: 72px;
    letter-spacing: 4px;
    line-height: 1;
    color: var(--brand-ink);
  }
  .size-block {
    position: absolute;
    left: 70px;
    bottom: 80px;
  }
  .size-label {
    font-size: 36px;
    font-weight: 400;
    line-height: 1.1;
    color: var(--label-ink);
  }
  .size-value {
    margin-left: 20px;
    font-size: 76px;
    font-weight: 700;
    line-height: 1;
    color: var(--size-grey);
  }
</style>
</head>
<body>
<main class="canvas">
  <section class="tag size-tag" aria-label="Waistband size label, blank back">
    <span class="eyelet"></span>
  </section>

  <section class="tag main-tag" aria-label="Tarvo main hang label">
    <div class="wave-artwork" role="img" aria-label="Decorative dripping wave artwork with a red glow and white highlight"></div>
    <span class="eyelet"></span>
    <h1 class="brand-name">TARVO</h1>
    <div class="size-block">
      <p class="size-label">Size:</p>
      <p class="size-value">32x32</p>
    </div>
  </section>
</main>
</body>
</html>
```